Design concept for BrightKestrel.com Support Page

We are about to launch a new support page for our www.brightkestrel.com service for photographers and visual artists. The service provides media management, cloud storage, promotional and secure distribution to our members.

The support page will include FAQs and video tutorials.

In particular we're looking for a header for this page that suggests the user is in the support area of our service - so perhaps an illustration that suggests support could look nice (perhaps repair man or doctor iconography). Something to give this area of our site a different look and something that looks both cool and friendly.

Currently the page looks distinctly sparse and undesigned (see attached screenshot) - something that could be remedied, we feel, by some subtle design enhancements that we can implement using CSS.

```html
<!DOCTYPE html>
<html lang="en">
<head>
<meta charset="utf-8">
<title>BrightKestrel Support</title>
<link href="https://fonts.googleapis.com/css2?family=Open+Sans:wght@300;400;600;700&display=swap" rel="stylesheet">
<style>
:root{
  --white:#ffffff;
  --ink:#4a4a4a;
  --muted:#7a7a7a;
  --answer:#666666;
  --rule:#dedede;
  --hero:#77a5a8;
  --hero-sub:#f6c680;
  --orange:#f47b20;
  --question:#e2572b;
  --dark:#262626;
  --darker:#121212;
  --footer-link:#b8b8b8;
  --footer-dim:#666666;
}
*{margin:0;padding:0;box-sizing:border-box}
html,body{width:836px;height:1200px;overflow:hidden;background:var(--white)}
body{font-family:"Open Sans",sans-serif;color:var(--ink);position:relative}

.site-header{position:absolute;top:0;left:0;width:836px;height:70px;background:var(--white)}
.brand{position:absolute;left:70px;top:17px;display:flex;align-items:center;gap:8px;font-weight:700;font-size:24px;color:#555;letter-spacing:-.3px}
.brand-mark{width:20px;height:20px;border-radius:50%;background:var(--orange)}
.search-btn{position:absolute;left:634px;top:20px;width:26px;height:26px;background:#3a3a3a;border-radius:2px;display:flex;align-items:center;justify-content:center}
.user{position:absolute;left:678px;top:17px;display:flex;align-items:center;gap:8px;font-size:10px;color:#444}
.avatar{width:28px;height:28px;border-radius:50%;background:linear-gradient(135deg,#8a7a70,#3b3330)}

.hero{position:absolute;top:70px;left:0;width:836px;height:177px;background:var(--hero)}
.hero h1{position:absolute;left:71px;top:38px;font-weight:300;font-size:37px;color:var(--white);letter-spacing:-.3px}
.hero h2{position:absolute;left:71px;top:88px;font-weight:400;font-size:26px;color:var(--hero-sub)}
.hero-art{position:absolute;left:568px;top:8px;width:192px;height:162px;background:linear-gradient(160deg,#8fb7b9,#6a9a9d);border-radius:4px}

.intro{position:absolute;top:272px;left:118px;width:600px;text-align:center;font-size:12px;line-height:19px;color:var(--muted)}
.divider{position:absolute;top:341px;left:70px;width:696px;height:1px;background:var(--rule)}

.faq-title{position:absolute;top:372px;left:69px;font-weight:400;font-size:27px;color:var(--orange)}
.view-all{position:absolute;top:383px;right:70px;font-size:12px;color:#333;text-decoration:none}
.faq{position:absolute;left:70px;width:696px;border:1px solid var(--rule);border-radius:2px;padding:14px 20px 0 19px}
.faq .q,.faq .a{display:flex}
.faq .q{font-size:12px;color:var(--question);line-height:16px}
.faq .a{margin-top:9px;font-size:10.3px;line-height:16px;color:var(--answer)}
.faq .label{width:24px;flex:none}
.faq .a .label{color:#333;font-size:11px}

.tutorials{position:absolute;top:858px;left:0;width:836px;height:236px;background:var(--dark)}
.tutorials h2{text-align:center;margin-top:22px;font-weight:400;font-size:27px;color:var(--orange)}
.slider-arrow{position:absolute;top:93px;width:40px;height:51px;background:#161616;display:flex;align-items:center;justify-content:center}
.slider-arrow.prev{left:0}
.slider-arrow.next{right:0}
.video{position:absolute;top:80px;width:160px;text-align:center}
.thumb{width:160px;height:99px;position:relative;display:flex;align-items:center;justify-content:center}
.video p{margin-top:14px;font-size:9.6px;line-height:14px;color:#e8e8e8}

.site-footer{position:absolute;top:1094px;left:0;width:836px;height:106px;background:var(--darker);text-align:center}
.footer-nav{margin-top:23px;font-size:9.2px;color:var(--footer-link);letter-spacing:.2px}
.footer-nav span.sep{margin:0 6px}
.copyright{margin-top:17px;font-size:9px;color:#eee}
.powered{margin-top:2px;font-size:8.6px;color:var(--footer-dim)}
</style>
</head>
<body>

<header class="site-header">
  <div class="brand"><span class="brand-mark"></span>BrightKestrel</div>
  <div class="search-btn">
    <svg width="12" height="12" viewBox="0 0 12 12"><circle cx="5" cy="5" r="3.6" fill="none" stroke="#fff" stroke-width="1.6"/><line x1="7.6" y1="7.6" x2="11" y2="11" stroke="#fff" stroke-width="1.8" stroke-linecap="round"/></svg>
  </div>
  <div class="user"><span class="avatar" role="img" aria-label="User profile photo"></span>Mara Ellison</div>
</header>

<section class="hero">
  <h1>We’re Happy To Help...</h1>
  <h2>BrightKestrel Support</h2>
  <div class="hero-art" role="img" aria-label="Illustration of a cheerful repairman with a wrench beside a happy user on an office chair"></div>
</section>

<p class="intro">Aliquam erat volutpat. Etiam luctus rutrum diam sit amet egestas. Mauris et odio nisl. Cras vulputate mi quis neque venenatis, vitae lacinia magna euismod. Aliquam tincidunt velit et diam mattis iaculis.</p>
<div class="divider"></div>

<h2 class="faq-title">FAQ’s</h2>
<a class="view-all" href="#">View All »</a>

<article class="faq" style="top:415px;height:105px">
  <div class="q"><span class="label">Q :</span><span>Pellentesque habitant morbi tristique senectus et netus et malesuada fames ac turpis egestas?</span></div>
  <div class="a"><span class="label">A :</span><span>Nam a malesuada libero. Duis sodales et libero vel interdum. Interdum et malesuada fames ac ante ipsum primis in faucibus. Donec lobortis dui tortor, eu lobortis felis mattis nec. Sed justo quam, luctus eu mauris eget, euismod dapibus sem. Sed tempus feugiat ante, at ornare libero volutpat sed.</span></div>
</article>

<article class="faq" style="top:540px;height:141px">
  <div class="q"><span class="label">Q :</span><span>Aliquam scelerisque mauris dui, ut sollicitudin metus feugiat a?</span></div>
  <div class="a"><span class="label">A :</span><span>Maecenas sagittis mauris ac malesuada imperdiet. Phasellus elit sem, venenatis a ligula ac, posuere dapibus magna. Mauris vehicula turpis enim, sit amet fermentum elit rutrum nec. Sed enim risus, facilisis eget eros eget, imperdiet cursus urna. Cras ut laoreet eros. Mauris in porta orci. Proin id viverra nisi, vitae volutpat est. Vestibulum eu rhoncus turpis. Proin vitae venenatis lacus, eget viverra dui. Vivamus semper diam sollicitudin ligula condimentum, id molestie tortor auctor. Vivamus blandit nisl leo, sit amet egestas arcu aliquam vel. Integer nec felis non mi consequat interdum.</span></div>
</article>

<article class="faq" style="top:700px;height:105px">
  <div class="q"><span class="label">Q :</span><span>Pellentesque habitant morbi tristique senectus et netus et malesuada fames ac turpis egestas?</span></div>
  <div class="a"><span class="label">A :</span><span>Nam a malesuada libero. Duis sodales et libero vel interdum. Interdum et malesuada fames ac ante ipsum primis in faucibus. Donec lobortis dui tortor, eu lobortis felis mattis nec. Sed justo quam, luctus eu mauris eget, euismod dapibus sem. Sed tempus feugiat ante, at ornare libero volutpat sed.</span></div>
</article>

<section class="tutorials">
  <h2>Video Tutorials</h2>
  <div class="slider-arrow prev"><svg width="16" height="30" viewBox="0 0 16 30"><polyline points="14,1 2,15 14,29" fill="none" stroke="#ddd" stroke-width="1.4"/></svg></div>
  <div class="slider-arrow next"><svg width="16" height="30" viewBox="0 0 16 30"><polyline points="2,1 14,15 2,29" fill="none" stroke="#ddd" stroke-width="1.4"/></svg></div>

  <div class="video" style="left:70px">
    <div class="thumb" role="img" aria-label="Illustration of a hand cursor pressing an upload button" style="background:linear-gradient(180deg,#cfd3d5,#b9bec1)">
      <svg width="36" height="36" viewBox="0 0 36 36"><circle cx="18" cy="18" r="16" fill="none" stroke="#fff" stroke-width="2.4"/><polygon points="14,10 27,18 14,26" fill="#fff"/></svg>
    </div>
    <p>Uploading Files Using the<br>Drang and Drop Uploader</p>
  </div>
  <div class="video" style="left:250px">
    <div class="thumb" role="img" aria-label="Illustration of people arranging photos on a large tablet" style="background:linear-gradient(180deg,#eef0f2,#d6d9dd)">
      <svg width="36" height="36" viewBox="0 0 36 36"><circle cx="18" cy="18" r="16" fill="none" stroke="#fff" stroke-width="2.4"/><polygon points="14,10 27,18 14,26" fill="#fff"/></svg>
    </div>
    <p>Publising Files</p>
  </div>
  <div class="video" style="left:428px">
    <div class="thumb" role="img" aria-label="Illustration of a person at a desk building web galleries" style="background:linear-gradient(180deg,#7fb0b3,#5f9598)">
      <svg width="36" height="36" viewBox="0 0 36 36"><circle cx="18" cy="18" r="16" fill="none" stroke="#fff" stroke-width="2.4"/><polygon points="14,10 27,18 14,26" fill="#fff"/></svg>
    </div>
    <p>Creating Galleries</p>
  </div>
  <div class="video" style="left:606px">
    <div class="thumb" role="img" aria-label="Illustration of portfolio tools, charts and a target on coloured tiles" style="background:linear-gradient(135deg,#4a8cc0,#2f6a9a 55%,#e8b640)">
      <svg width="36" height="36" viewBox="0 0 36 36"><circle cx="18" cy="18" r="16" fill="none" stroke="#fff" stroke-width="2.4"/><polygon points="14,10 27,18 14,26" fill="#fff"/></svg>
    </div>
    <p>Creating Portfolios</p>
  </div>
</section>

<footer class="site-footer">
  <nav class="footer-nav">
    Home<span class="sep">·</span>Contact Us<span class="sep">·</span>Affiliate Program<span class="sep">·</span>Privacy Policy<span class="sep">·</span>Site Terms and Conditions<span class="sep">·</span>About Us
  </nav>
  <p class="copyright">© Copyright 2014 Northvale Images Pte Ltd. All rights reserved.</p>
  <p class="powered">Powered by BrightKestrel</p>
</footer>

</body>
</html>
```